Marlowe Holdings LLC - Business Cards

Need the following information on the cards:

Name: Dean R Vossler
Title: Chief Executive Manager

Business address:
412 N Ridgeview Lane #118
Carol Stream, Il 60412

Phone: (630) 555-0148 - Business
KPV FFL license number: 5-21-xxx-xx-xx-04519
Email: dean.vossler@marloweholdingsffl.com

Target Market(s)

Firearm owners

Industry/Entity Type

Firearms industry,

Contact Information for Business Card

Contact number, name and title, web page address, email, business address and kpv license number,

Requirements
Must have
• Name, title, business address, phone numbers, KPV license numbers, web page address and email address.
Nice to have
• Cellphone number,

```html
<!DOCTYPE html>
<html lang="en">
<head>
<meta charset="utf-8">
<title>Marlowe Holdings LLC – Business Cards</title>
<link rel="stylesheet" href="https://fonts.googleapis.com/css2?family=Open+Sans:wght@400;600;700&display=swap">
<style>
  :root {
    --backdrop: #e4e5e7;
    --card: #ffffff;
    --ink: #1d1d1f;
    --brand-red: #e3151d;
    --rule: #222222;
    --muted: #3a3a3a;
  }
  * { box-sizing: border-box; margin: 0; padding: 0; }
  html, body {
    width: 1200px; height: 800px; overflow: hidden;
    background: var(--backdrop);
    font-family: "Open Sans", Arial, sans-serif;
    color: var(--ink);
  }
  .canvas {
    position: relative; width: 1200px; height: 800px;
    display: flex; align-items: center; justify-content: center; gap: 50px;
  }
  .card {
    position: relative; width: 540px; height: 309px;
    background: var(--card);
    box-shadow: 0 2px 10px rgba(0,0,0,.12);
  }

  /* Front */
  .card--front { display: flex; align-items: center; justify-content: center; }
  .wordmark {
    font-weight: 700; color: var(--brand-red);
    text-transform: uppercase; text-align: center; line-height: 1.05;
  }
  .card--front .wordmark { font-size: 34px; letter-spacing: 2px; }
  .card--front .wordmark span { display: block; font-size: 15px; letter-spacing: 5px; }

  /* Back */
  .brand-block {
    position: absolute; left: 32px; top: 28px; width: 190px; height: 170px;
    display: flex; align-items: center; gap: 10px;
  }
  .brand-dot { width: 22px; height: 22px; border-radius: 50%; background: var(--brand-red); flex: none; }
  .card--back .wordmark { font-size: 19px; text-align: left; letter-spacing: 1px; }
  .card--back .wordmark span { display: block; font-size: 10px; letter-spacing: 2.5px; }

  .divider {
    position: absolute; left: 262px; top: 40px; width: 2px; height: 150px; background: var(--rule);
  }
  .contact { position: absolute; left: 292px; top: 62px; width: 230px; }
  .contact__name { color: var(--brand-red); font-size: 21px; font-weight: 600; }
  .contact__title { font-size: 10.5px; color: var(--muted); margin: 2px 0 12px; }
  .contact__row { display: flex; gap: 8px; font-size: 13px; line-height: 1.35; margin-bottom: 8px; }
  .contact__row svg { flex: none; margin-top: 2px; }

  .info-band { position: absolute; left: 18px; right: 18px; top: 222px; }
  .info-band__rule { display: block; width: 100%; height: 3px; }
  .info-band__text {
    display: flex; justify-content: space-between; align-items: center;
    font-size: 11.5px; padding: 5px 14px 5px;
  }
  .license { font-weight: 600; }
</style>
</head>
<body>
<main class="canvas">
  <section class="card card--front" aria-label="Card front">
    <div class="wordmark">Marlowe<span>Holdings LLC</span></div>
  </section>

  <section class="card card--back" aria-label="Card back">
    <div class="brand-block">
      <span class="brand-dot"></span>
      <div class="wordmark">Marlowe<span>Holdings LLC</span></div>
    </div>

    <div class="divider"></div>

    <div class="contact">
      <p class="contact__name">Dean R Vossler</p>
      <p class="contact__title">Chief Executive Manager</p>
      <div class="contact__row">
        <svg width="12" height="14" viewBox="0 0 12 14" aria-hidden="true">
          <circle cx="6" cy="6" r="6" fill="var(--brand-red)"/>
          <circle cx="6" cy="5.5" r="2" fill="#fff"/>
        </svg>
        <p>412 N Ridgeview Lane #118<br>Carol Stream, Il 60412</p>
      </div>
      <div class="contact__row">
        <svg width="12" height="14" viewBox="0 0 12 14" aria-hidden="true">
          <path d="M3 1.5 5 4 3.8 5.5c.6 1.4 1.6 2.5 3 3.2L8.3 7.6 11 9.5 9.6 12C5 11.5 1.5 7.5 1 3Z" fill="none" stroke="var(--brand-red)" stroke-width="1.4" stroke-linejoin="round"/>
        </svg>
        <p>(630) 555-0148</p>
      </div>
    </div>

    <div class="info-band">
      <svg class="info-band__rule" viewBox="0 0 500 3" preserveAspectRatio="none" aria-hidden="true">
        <polygon points="0,1.5 250,0 500,1.5 250,3" fill="var(--rule)"/>
      </svg>
      <div class="info-band__text">
        <span class="license">KPV FFL license number: 5-21-xxx-xx-xx-04519</span>
        <span class="email">dean.vossler@marloweholdingsffl.com</span>
      </div>
      <svg class="info-band__rule" viewBox="0 0 500 3" preserveAspectRatio="none" aria-hidden="true">
        <polygon points="0,1.5 250,0 500,1.5 250,3" fill="var(--rule)"/>
      </svg>
    </div>
  </section>
</main>
</body>
</html>
```